We need a redesign of our current website: www.vallowmerehosts.com. Vallowmere Holdings is a fully integrated hospitality development, management, and investment firm. We strive for leadership in each of our segments by building quality assets, exacting high standards of customer service, and focusing on returns for our investors and partners.

It is our mission to provide our guests an exceptional lodging experience; our clients an unsurpassed level of management in their properties; and create positive returns for our investors and partners. We achieve our mission via a company culture of transparency, ownership of our actions, and accountability for our results.

Target Market(s)

hotel owners, hotel developers, hotel investors, bankers

Industry/Entity Type

Hospitality

Requirements
Must have
• Our logo has to be there along with the quote and the ability to convey the following quote off of our current website: "Vallowmere was founded on the principles of integrity, honesty, loyalty, and trust. These convictions embody our company at every level, and show in every action."

```html
<!DOCTYPE html>
<html lang="en">
<head>
<meta charset="utf-8">
<title>Vallowmere Holdings</title>
<link rel="stylesheet" href="https://fonts.googleapis.com/css2?family=Roboto+Condensed:wght@300;400&family=Arimo:wght@400;700&display=swap">
<style>
  :root {
    --orange: #f28c1e;
    --orange-dark: #e07a10;
    --ink: #222;
    --text: #555;
    --muted: #666;
    --card: #ebebeb;
    --quote-bg: #f2f2f2;
    --footer-bg: #fde4cb;
    --hero-top: #ead9b8;
    --hero-bottom: #fdfaf4;
    --nav-bg: #000;
  }
  * { box-sizing: border-box; margin: 0; padding: 0; }
  html, body { width: 1045px; height: 1200px; overflow: hidden; background: #fff; }
  body { position: relative; font-family: "Arimo", Arial, sans-serif; color: var(--text); }

  .hero {
    position: absolute; left: 0; top: 0; width: 1045px; height: 437px;
    background: linear-gradient(180deg, var(--hero-top) 0%, #f4e9d6 45%, var(--hero-bottom) 100%);
    border-bottom: 1px solid #f3d7b0;
  }
  .brand {
    position: absolute; left: 0; top: 22px; display: flex; align-items: center; gap: 12px;
  }
  .brand-mark { width: 46px; height: 46px; border-radius: 50%; background: var(--orange); }
  .brand-name {
    font-family: "Roboto Condensed", "Arial Narrow", sans-serif; font-weight: 400;
    font-size: 34px; color: var(--orange); letter-spacing: 1px;
  }
  .main-nav {
    position: absolute; right: 0; top: 23px; height: 56px; display: flex;
    background: var(--nav-bg); border-radius: 3px 3px 3px 3px;
  }
  .main-nav a {
    position: relative; display: block; padding: 0 18px; line-height: 56px;
    font-family: "Roboto Condensed", "Arial Narrow", sans-serif; font-size: 21px;
    color: #fff; text-decoration: none; border-left: 1px solid #222;
  }
  .main-nav a:first-child { border-left: 0; }
  .main-nav a.is-active { background: var(--orange); border-radius: 3px 0 0 3px; }
  .main-nav a.is-active::after {
    content: ""; position: absolute; left: 50%; bottom: -8px; margin-left: -8px;
    border-left: 8px solid transparent; border-right: 8px solid transparent; border-top: 8px solid var(--orange);
  }
  .hero-title {
    position: absolute; left: 2px; top: 224px;
    font-family: "Roboto Condensed", "Arial Narrow", sans-serif; font-weight: 300;
    font-size: 41px; color: #555;
  }
  .hero-art {
    position: absolute; left: 680px; top: 112px; width: 365px; height: 325px;
    background: radial-gradient(ellipse at 45% 40%, rgba(60,60,60,0.35) 0%, rgba(120,110,95,0.18) 45%, rgba(240,225,200,0) 75%);
  }

  .services { position: absolute; left: 0; top: 463px; width: 1045px; height: 352px; }
  .service-card {
    position: absolute; top: 0; width: 335px; height: 352px;
    background: var(--card); border-top: 4px solid var(--orange);
  }
  .service-card:nth-child(1) { left: 0; }
  .service-card:nth-child(2) { left: 355px; }
  .service-card:nth-child(3) { left: 710px; }
  .service-title {
    position: absolute; left: 15px; top: 13px;
    font-family: "Roboto Condensed", "Arial Narrow", sans-serif; font-size: 21px; font-weight: 400;
    color: var(--orange);
  }
  .service-image { position: absolute; left: 16px; top: 43px; width: 304px; height: 168px; }
  .img-bulbs { background: linear-gradient(180deg, #fff 0%, #f3f3f3 60%, #d9d9d9 100%); }
  .img-puzzle { background: linear-gradient(135deg, #2a2a2a 0%, #11141c 50%, #c9a48a 100%); }
  .img-sprout { background: radial-gradient(ellipse at 50% 70%, #c9a76a 0%, #e8dcc2 35%, #fff 65%); }
  .service-text {
    position: absolute; left: 16px; top: 224px; width: 304px;
    font-size: 12.5px; line-height: 19.5px; color: var(--text);
  }
  .service-text strong { color: #444; }
  .read-more {
    position: absolute; right: 16px; bottom: 0; width: 103px; height: 31px;
    background: var(--orange); color: #fff; font-size: 13px; font-weight: 700;
    text-decoration: none; display: flex; align-items: center; justify-content: center; gap: 5px;
  }

  .about { position: absolute; left: 0; top: 832px; width: 1045px; }
  .about h2 {
    font-family: "Roboto Condensed", "Arial Narrow", sans-serif; font-weight: 400;
    font-size: 28px; color: var(--orange); padding-bottom: 10px;
    border-bottom: 1px dashed #ddd;
  }
  .about p { font-size: 12.5px; line-height: 18px; color: var(--text); margin-top: 13px; }
  .about p + p { margin-top: 13px; }

  .quote {
    position: absolute; left: 0; top: 1002px; width: 1045px; height: 126px;
    background: var(--quote-bg); border-top: 3px solid var(--orange);
  }
  .quote h3 {
    position: absolute; left: 15px; top: 12px;
    font-family: "Roboto Condensed", "Arial Narrow", sans-serif; font-weight: 400;
    font-size: 21px; color: var(--orange);
  }
  .quote blockquote {
    position: absolute; left: 15px; top: 47px; width: 1015px;
    font-size: 14.5px; line-height: 22px; font-weight: 700; color: var(--muted);
  }
  .quote cite {
    position: absolute; right: 18px; top: 94px;
    font-style: normal; font-size: 14.5px; font-weight: 700; color: var(--ink);
  }

  .site-footer {
    position: absolute; left: 0; top: 1153px; width: 1045px; height: 47px;
    background: var(--footer-bg); display: flex; align-items: center; justify-content: space-between;
    padding: 0 15px;
  }
  .footer-address { font-size: 12.5px; color: #444; }
  .footer-phone { font-family: "Roboto Condensed", "Arial Narrow", sans-serif; font-size: 17px; color: var(--ink); }
</style>
</head>
<body>
  <header class="hero">
    <div class="brand">
      <span class="brand-mark"></span>
      <span class="brand-name">VALLOWMERE HOLDINGS</span>
    </div>
    <nav class="main-nav">
      <a href="#" class="is-active">Home</a>
      <a href="#">Services</a>
      <a href="#">Projects</a>
      <a href="#">Team</a>
      <a href="#">Contact</a>
    </nav>
    <h1 class="hero-title">The Art and Science of Management</h1>
    <div class="hero-art" role="img" aria-label="Hand drawing a set of interlocking gears"></div>
  </header>

  <section class="services">
    <article class="service-card">
      <h2 class="service-title">Development</h2>
      <div class="service-image img-bulbs" role="img" aria-label="Row of light bulbs evolving from old filament to modern LED"></div>
      <p class="service-text"><strong>When evaluating sites</strong> for purchase and hotel development, our experienced team conducts the full array of feasibility studies and market analyses. Our development strategy focuses on...</p>
      <a href="#" class="read-more">Read more
        <svg width="6" height="8" viewBox="0 0 6 8"><path d="M1 1l3 3-3 3" stroke="#fff" stroke-width="1.6" fill="none"/></svg></a>
    </article>
    <article class="service-card">
      <h2 class="service-title">Management</h2>
      <div class="service-image img-puzzle" role="img" aria-label="Hands joining puzzle pieces together"></div>
      <p class="service-text"><strong>Using proven strategies</strong> we maximize potential and produce profitable results for your hotel, just as we do with our own. Our management teams are empowered with the tools, training...</p>
      <a href="#" class="read-more">Read more
        <svg width="6" height="8" viewBox="0 0 6 8"><path d="M1 1l3 3-3 3" stroke="#fff" stroke-width="1.6" fill="none"/></svg></a>
    </article>
    <article class="service-card">
      <h2 class="service-title">Investment</h2>
      <div class="service-image img-sprout" role="img" aria-label="Young green sprout growing from a pile of coins"></div>
      <p class="service-text"><strong>Vallowmere recognizes</strong> that we are entrusted with investors' capital. In honoring this trust we aim to create and realize shareholder value through the acquisition, development, and management...</p>
      <a href="#" class="read-more">Read more
        <svg width="6" height="8" viewBox="0 0 6 8"><path d="M1 1l3 3-3 3" stroke="#fff" stroke-width="1.6" fill="none"/></svg></a>
    </article>
  </section>

  <section class="about">
    <h2>About Vallowmere Holdings</h2>
    <p>Vallowmere Holdings is a fully integrated hospitality development, management, and investment firm. We strive for leadership in each of our segments by building quality assets, exacting high standards of customer service, and focusing on returns for our investors and partners.</p>
    <p>It is our mission to provide our guests an exceptional lodging experience; our clients an unsurpassed level of management in their properties; and create positive returns for our investors and partners. We achieve our mission via a company culture of transparency, ownership of our actions, and accountability for our results.</p>
  </section>

  <section class="quote">
    <h3>Creating Exceptional Experiences.</h3>
    <blockquote>"Vallowmere was founded on the principles of integrity, honesty, loyalty, and trust. These convictions embody our company at every level, and show in every action."</blockquote>
    <cite>-Dev Marlowe, President and CEO</cite>
  </section>

  <footer class="site-footer">
    <span class="footer-address">4810 Harlan Crossing Dr. #212, Ashbury, OH 45102</span>
    <span class="footer-phone">Phone : 555.310.2741</span>
  </footer>
</body>
</html>
```